Holistic Therapy (aromatherapy, massage, reflexology, life coaching, soul healing, aura reading)

I work for myself as a holistic therapist doing: aromatherapy massage, massage, reflexology, abdominal-sacral massage, life coaching, soul healing, aura readings. I want a business card that doesn't focus on any one of these( so not just feet or a massage couch,but rather a card that creates the feeling of wholeness, healing, health and which can encompass all my therapies - e.g. green or purple are colours I like (especially green, or maybe green on back and purple on front). It's going to be called Rosa Elwin Therapies. I don't want to list all my therapies on the card in case I add others later.). At some point I will create a website but in this instance I just want to get some cards printed to get 'out there' while I design my website.
Updates

Hi, thanks for all your designs. Can you find a way to include the therapies that I offer within the card, either on the front or back…the therapies I offer are: aromatherapy massage, reflexology, swedish body massage, abdominal-sacral massage, nutrition, soul healing, aura readings. (Maybe have them with a bullet point before each?) I am not sure whether they should be on the front of the card or the back or whether having them would spoil the card but it occurred to me that just having rosa elwin therapies doesn't tell people what therapies I offer, hence the new idea to list them somehow…)

Target Market(s)

Mainly women (middle class probably with disposable incomes).

Industry/Entity Type

Massage

Contact Information for Business Card

Rosa Elwin Therapies, Tel: 07942 586113, email: vitalbloom@mailvane.com, (on back of card I want: Rosalind Elwin BScHons, OKQRB, GPCL.)

Requirements
Nice to have
• A logo for Rosa Elwin Therapies would be good.

```html
<!DOCTYPE html>
<html lang="en">
<head>
<meta charset="utf-8">
<title>Rosa Elwin Therapies – Business Card</title>
<link rel="stylesheet" href="https://fonts.googleapis.com/css2?family=EB+Garamond:wght@400;500&display=swap">
<style>
  :root {
    --page-bg: #ffffff;
    --ink: #1c3a33;
    --mark: #1a3b33;
    --grass-deep: #7fbf9e;
    --grass-mid: #a9d6bd;
    --grass-light: #d9eee2;
    --text-shadow: rgba(0, 0, 0, 0.35);
  }
  html, body {
    margin: 0;
    padding: 0;
    width: 1200px;
    height: 1000px;
    overflow: hidden;
    background: var(--page-bg);
  }
  .canvas {
    position: relative;
    width: 1200px;
    height: 1000px;
  }
  .card {
    position: absolute;
    left: 81px;
    top: 157px;
    width: 1039px;
    height: 684px;
    overflow: hidden;
  }
  .card-backdrop {
    position: absolute;
    inset: 0;
    background:
      radial-gradient(ellipse 40% 30% at 10% 50%, var(--grass-deep), transparent 70%),
      radial-gradient(ellipse 35% 25% at 90% 45%, var(--grass-deep), transparent 70%),
      radial-gradient(ellipse 50% 40% at 55% 20%, var(--grass-light), transparent 70%),
      radial-gradient(ellipse 40% 30% at 40% 90%, var(--grass-light), transparent 70%),
      linear-gradient(160deg, var(--grass-mid), var(--grass-light) 50%, var(--grass-mid));
  }
  .brand-square {
    position: absolute;
    left: 407px;
    top: 76px;
    width: 226px;
    height: 229px;
    background: var(--mark);
  }
  .card-text {
    position: absolute;
    left: 0;
    width: 100%;
    margin: 0;
    text-align: center;
    font-family: "EB Garamond", Georgia, serif;
    font-weight: 400;
    color: var(--ink);
    text-shadow: 1px 2px 2px var(--text-shadow);
  }
  .business-name {
    top: 308px;
    font-size: 52px;
    line-height: 56px;
    letter-spacing: -0.5px;
  }
  .contact {
    top: 508px;
    font-size: 42px;
    line-height: 60px;
  }
  .contact span { display: block; }
</style>
</head>
<body>
<div class="canvas">
  <section class="card">
    <div class="card-backdrop" role="img" aria-label="Soft-focus photograph of pale green grass blades"></div>
    <div class="brand-square" role="img" aria-label="Decorative illuminated initial ornament"></div>
    <h1 class="card-text business-name">Rosa Elwin<br>Therapies</h1>
    <p class="card-text contact">
      <span class="contact-phone">Tel: 07942 586113</span>
      <span class="contact-email">email: vitalbloom@mailvane.com</span>
    </p>
  </section>
</div>
</body>
</html>
```